Mission Vision and Values Infographic

We are a healthcare organisation and would like to create a graphic which showcases our Mission, Vision and Values in a clear and beautiful manner.

Attached is:

* Our mission vision and values.
* Style Guide
* Examples of other designs found on the web
* Logo

Your design should be Simple, Clear, Professional and Beautiful.

If you prefer, you can submit a Basic design to start off with for initial feedback before then refining in a future submission. Please check back in the comments section as I will be providing additional general remarks if needed.

The design needs to be created in a tool which will then allow us to modify it in the future…. Ideally either Adobe InDesign, Adobe Illustrator or Adobe Photoshop. Vector is preferred.

All together, the whole design needs to be:

* Printable on one sheet of A3 size paper (to go on our wall)
* Be able to go on a webpage

So there might be slight variations for bigger and smaller displays. For example, the A3 Page will have all three - Mission, Vision and Values + Logo together. The version for a webpage might be separated into 3 parts to make it easier to show on a webpage.

Good luck and happy designing

```html
<!DOCTYPE html>
<html lang="en">
<head>
<meta charset="utf-8">
<title>Harbour Voice Clinic – Vision, Mission and Core Values</title>
<link href="https://fonts.googleapis.com/css2?family=Montserrat:wght@600;700;800&display=swap" rel="stylesheet">
<style>
:root{
  --navy:#1b4b8c;
  --sky:#29a8e0;
  --white:#ffffff;
  --purple:#5a1a57;
  --green:#4fae4a;
  --blue:#184a8c;
  --red:#a51b2b;
  --yellow:#f4b120;
  --ink:#1b4b8c;
}
*{box-sizing:border-box;margin:0;padding:0}
html,body{width:848px;height:1200px;overflow:hidden;background:var(--navy)}
.poster{
  position:relative;width:900px;height:1273px;
  transform:scale(0.94222);transform-origin:0 0;
  background:var(--navy);
  font-family:'Montserrat',Arial,sans-serif;
}
.sheet{position:absolute;left:30px;top:22px;width:842px;height:1226px;background:var(--white);border-radius:22px}
.brand{
  position:absolute;left:600px;top:0;width:196px;height:110px;background:var(--white);
  border-radius:0 0 14px 14px;display:flex;align-items:center;justify-content:flex-end;gap:10px;padding-right:14px;z-index:3;
}
.brand-dot{width:40px;height:40px;border-radius:50%;background:var(--sky);flex:none}
.brand-name{color:var(--sky);font-weight:700;font-size:19px;line-height:1.05;text-align:right}
.statement{
  position:absolute;left:70px;top:65px;width:760px;height:305px;background:var(--sky);
  border-radius:26px;padding:20px 30px 0 36px;color:var(--white);z-index:2;
}
.statement-title{display:flex;align-items:baseline;font-weight:800;font-size:33px;letter-spacing:.5px;line-height:1}
.statement-title .rule{flex:1;border-bottom:2px dashed var(--white);margin-left:4px;height:0;transform:translateY(-2px)}
.statement-title.vision .rule{max-width:235px}
.statement-text{font-weight:700;font-size:17.6px;line-height:1.28;margin:8px 0 14px;text-align:left}
.wheel{position:absolute;left:0;top:0;width:900px;height:1273px}
.value{
  position:absolute;width:210px;height:210px;border-radius:50%;color:var(--white);
  display:flex;flex-direction:column;align-items:center;padding:14px 26px 0;text-align:center;z-index:2;
}
.value h2{font-weight:800;font-size:20px;letter-spacing:.3px;padding-bottom:3px;border-bottom:1px solid rgba(255,255,255,.7);margin-bottom:6px}
.value p{font-weight:600;font-size:12.4px;line-height:1.28}
.value.quality{left:347px;top:400px;background:var(--purple)}
.value.integrity{left:604px;top:567px;background:var(--green)}
.value.diversity{left:617px;top:833px;background:var(--blue)}
.value.flexibility{left:347px;top:1035px;background:var(--red)}
.value.positivity{left:87px;top:835px;background:var(--sky)}
.value.creativity{left:87px;top:555px;background:var(--yellow)}
.value.positivity p,.value.diversity p{margin-top:8px}
.hub{
  position:absolute;left:340px;top:728px;width:224px;height:224px;border-radius:50%;
  background:var(--white);border:13px solid var(--sky);display:flex;align-items:center;justify-content:center;
  text-align:center;color:var(--ink);font-weight:700;font-size:39px;line-height:1.12;z-index:2;
}
.hub span{display:block}
</style>
</head>
<body>
<div class="poster">
  <div class="sheet"></div>

  <div class="brand">
    <div class="brand-name">Harbour<br>Voice<br>Clinic</div>
    <div class="brand-dot"></div>
  </div>

  <section class="statement">
    <h1 class="statement-title vision">OUR VISION<span class="rule"></span></h1>
    <p class="statement-text">Individuals of all abilities will have the opportunity to achieve their thera-py goals by accessing gold standard services, so they may confidently participate in the wider community where they will be understood, sup-ported and embraced for their individuality.</p>
    <h1 class="statement-title mission">OUR MISSION<span class="rule"></span></h1>
    <p class="statement-text">At Harbour Voice Clinic we strive to ensure our clients and families have access to high quality, evidence-based intervention from a pas-sionate and professional team to improve and develop individual func-tional skills that contribute to successful participation in the community.</p>
  </section>

  <svg class="wheel" viewBox="0 0 900 1273" aria-hidden="true">
    <g transform="translate(452 840)">
      <circle r="321" fill="none" stroke="#29a8e0" stroke-width="58"/>
      <g class="segments">
        <path d="M-45,-111 L-103.5,-222 L103.5,-222 L45,-111 Z" fill="#5a1a57"/>
        <path transform="rotate(60)" d="M-45,-111 L-103.5,-222 L103.5,-222 L45,-111 Z" fill="#4fae4a"/>
        <path transform="rotate(120)" d="M-45,-111 L-103.5,-222 L103.5,-222 L45,-111 Z" fill="#184a8c"/>
        <path transform="rotate(180)" d="M-45,-111 L-103.5,-222 L103.5,-222 L45,-111 Z" fill="#a51b2b"/>
        <path transform="rotate(240)" d="M-45,-111 L-103.5,-222 L103.5,-222 L45,-111 Z" fill="#29a8e0"/>
        <path transform="rotate(300)" d="M-45,-111 L-103.5,-222 L103.5,-222 L45,-111 Z" fill="#f4b120"/>
      </g>
      <g class="segment-icons" fill="none" stroke="rgba(255,255,255,.55)" stroke-width="2">
        <rect x="-24" y="-186" width="48" height="48" rx="10" role="img" aria-label="Quality icon"/>
        <rect transform="rotate(60)" x="-24" y="-186" width="48" height="48" rx="10" role="img" aria-label="Integrity icon"/>
        <rect transform="rotate(120)" x="-24" y="-186" width="48" height="48" rx="10" role="img" aria-label="Diversity icon"/>
        <rect transform="rotate(180)" x="-24" y="-186" width="48" height="48" rx="10" role="img" aria-label="Flexibility icon"/>
        <rect transform="rotate(240)" x="-24" y="-186" width="48" height="48" rx="10" role="img" aria-label="Positivity icon"/>
        <rect transform="rotate(300)" x="-24" y="-186" width="48" height="48" rx="10" role="img" aria-label="Creativity icon"/>
      </g>
      <g class="cycle-arrows" fill="none" stroke-width="2.5" stroke-linecap="round" stroke-linejoin="round">
        <g transform="rotate(30)" stroke="#5a1a57"><path d="M-56.1,-264.1 A270,270 0 0 1 56.1,-264.1"/><polyline points="47.9,-272.9 56.1,-264.1 45.1,-259.4"/></g>
        <g transform="rotate(90)" stroke="#4fae4a"><path d="M-56.1,-264.1 A270,270 0 0 1 56.1,-264.1"/><polyline points="47.9,-272.9 56.1,-264.1 45.1,-259.4"/></g>
        <g transform="rotate(150)" stroke="#184a8c"><path d="M-56.1,-264.1 A270,270 0 0 1 56.1,-264.1"/><polyline points="47.9,-272.9 56.1,-264.1 45.1,-259.4"/></g>
        <g transform="rotate(210)" stroke="#a51b2b"><path d="M-56.1,-264.1 A270,270 0 0 1 56.1,-264.1"/><polyline points="47.9,-272.9 56.1,-264.1 45.1,-259.4"/></g>
        <g transform="rotate(270)" stroke="#29a8e0"><path d="M-56.1,-264.1 A270,270 0 0 1 56.1,-264.1"/><polyline points="47.9,-272.9 56.1,-264.1 45.1,-259.4"/></g>
        <g transform="rotate(330)" stroke="#f4b120"><path d="M-56.1,-264.1 A270,270 0 0 1 56.1,-264.1"/><polyline points="47.9,-272.9 56.1,-264.1 45.1,-259.4"/></g>
      </g>
    </g>
  </svg>

  <div class="hub"><div><span>OUR</span><span>CORE</span><span>VALUES</span></div></div>

  <article class="value quality">
    <h2>QUALITY</h2>
    <p>We strive for excellence through evidence based practice, self-reflection, feedback and a continuous commitment to improvement and discovery both professionally and personally.</p>
  </article>
  <article class="value integrity">
    <h2>INTEGRITY</h2>
    <p>We care for and respect the needs and well-being of our families, our team and ourselves. We encourage openness, trust and honest communication at all times.</p>
  </article>
  <article class="value diversity">
    <h2>DIVERSITY</h2>
    <p>We embed diversity by recognising, respecting and appreciating differences in our families and our team.</p>
  </article>
  <article class="value flexibility">
    <h2>FLEXIBILITY</h2>
    <p>We are flexible in our problem solving and offer options and solutions for our families and team wherever we reasonably can.</p>
  </article>
  <article class="value positivity">
    <h2>POSITIVITY</h2>
    <p>We lead ourselves ‘above the line’ choosing to adopt a positive, accountable and solution-focused mindset.</p>
  </article>
  <article class="value creativity">
    <h2>CREATIVITY</h2>
    <p>We are innovative and collaborative, constantly workin towards new and improved ways to support our clients, families and our team.</p>
  </article>
</div>
</body>
</html>
```